Brindlecrest Risk & Planning Biz cards

**Brindlecrest Risk & Planning – Premium Business Card Design**

I am seeking a professional designer to create a luxury double-sided business card for Brindlecrest Risk & Planning, a retirement and wealth planning firm focused on helping families preserve wealth, reduce unnecessary taxes, protect assets, and create lasting legacies.

The card should reflect the image of a boutique wealth advisory firm or family office—not a traditional insurance salesperson. The overall feel should communicate trust, sophistication, stability, integrity, and long-term relationships.

**Brand Direction**

* Use the provided Brindlecrest Risk & Planning logo and brand assets.
* Color palette should be based on Brindlecrest's deep forest green, gold accents, and neutral tones.
* Design should be clean, elegant, and timeless.
* Avoid cluttered layouts, stock imagery, or overly aggressive sales-oriented designs.
* Emphasize premium whitespace and strong typography.

**Card Specifications**

* Standard U.S. business card size (3.5" x 2")
* Double-sided design
* Full-bleed print-ready files
* CMYK color format
* Include editable source files (AI, PSD, Canva, or similar)

**Preferred Print Finish**
The design should be optimized for:

* Velvet (soft-touch) finish
* Gold foil logo and accent elements
* Standard square corners
* Optional gold-painted edge compatibility if desired

**Front Side**

* Brindlecrest Risk & Planning logo prominently displayed
* Minimalist, high-end appearance
* Focus on branding and visual impact rather than excessive text

**Back Side**
Include:

* Dwight Hollander
* Founder & Financial Professional
* Phone Number
* Email Address
* QR Code (website or appointment scheduling page)

**Overall Inspiration**
Think:

* Private wealth management firm
* Boutique family office
* Estate planning attorney
* High-end financial advisory practice

The finished design should feel premium, memorable, and trustworthy while remaining understated and professional. The goal is for clients to immediately associate the Brindlecrest brand with confidence, stewardship, and long-term financial guidance.

Printer template for foil https://www.presslyquill.com/print-templates/foil-business-cards/

Target Market(s)

Foil should be used strategically on the Brindlecrest logo and select design elements. Deep forest green background with gold foil accents. Luxury wealth management / family office aesthetic. Clean, minimalist layout with ample whitespace. Professional and timeless appearance suitable for affluent clients and business owners.

Industry/Entity Type

Financial Services / Wealth Advisor

Contact Information for Business Card

* Dwight Hollander * Founder & Financial Professional * Phone Number * Email Address * Website * QR Code (website or appointment scheduling page)

Requirements
Must have
• Design must be optimized for Raised Gold Foil on Silk business cards.

```html
<!DOCTYPE html>
<html lang="en">
<head>
<meta charset="utf-8">
<title>Brindlecrest Risk &amp; Planning – Business Cards</title>
<link rel="stylesheet" href="https://fonts.googleapis.com/css2?family=Tinos:wght@400;700&family=Questrial&display=swap">
<style>
  :root {
    --backdrop: #232323;
    --card: #0f2a1f;
    --gold: #c9a24c;
    --white: #ffffff;
    --serif: "Tinos", "Times New Roman", serif;
    --sans: "Questrial", "Century Gothic", sans-serif;
  }
  * { margin: 0; padding: 0; box-sizing: border-box; }
  html, body { width: 1200px; height: 800px; overflow: hidden; }
  body {
    background: var(--backdrop);
    display: flex;
    align-items: center;
    justify-content: center;
    gap: 40px;
  }
  .card {
    position: relative;
    width: 540px;
    height: 309px;
    background: var(--card);
    overflow: hidden;
  }

  /* Brand lockup */
  .brand {
    display: flex;
    align-items: center;
    color: var(--gold);
    font-family: var(--serif);
    font-weight: 400;
    text-transform: uppercase;
  }
  .brand-dot { border-radius: 50%; background: var(--gold); flex: none; }
  .brand-name { line-height: 1.2; }
  .brand-tag { display: block; }

  /* Front */
  .card-front { display: flex; align-items: center; justify-content: center; }
  .card-front .brand { gap: 16px; }
  .card-front .brand-dot { width: 30px; height: 30px; }
  .card-front .brand-name { font-size: 34px; letter-spacing: 3px; }
  .card-front .brand-tag { font-size: 17px; letter-spacing: 5px; }

  /* Back */
  .card-back .brand { position: absolute; top: 32px; right: 34px; gap: 10px; }
  .card-back .brand-dot { width: 18px; height: 18px; }
  .card-back .brand-name { font-size: 20px; letter-spacing: 2px; }
  .card-back .brand-tag { font-size: 10px; letter-spacing: 3px; }

  .person { position: absolute; left: 40px; top: 112px; }
  .person-name {
    font-family: var(--serif);
    font-weight: 700;
    font-size: 22px;
    letter-spacing: 0.5px;
    color: var(--gold);
    text-transform: uppercase;
  }
  .person-role {
    font-family: var(--sans);
    font-size: 14px;
    color: var(--white);
    margin-top: 4px;
  }
  .divider {
    position: absolute;
    left: 40px; right: 34px; top: 172px;
    height: 1px;
    background: var(--white);
  }
  .contacts {
    position: absolute;
    left: 40px; top: 186px;
    list-style: none;
    font-family: var(--serif);
    font-size: 14px;
    color: var(--white);
  }
  .contacts li { display: flex; align-items: center; gap: 12px; height: 24px; }
  .contacts svg { width: 15px; height: 15px; fill: var(--gold); flex: none; }
  .address {
    position: absolute;
    right: 110px; top: 190px;
    text-align: right;
    font-family: var(--serif);
    font-size: 14px;
    line-height: 1.4;
    color: var(--white);
  }
  .qr-area {
    position: absolute;
    right: 34px; top: 186px;
    width: 62px; height: 62px;
    background: var(--gold);
  }
  .edge-band { position: absolute; left: 0; bottom: 0; width: 540px; height: 18px; }
</style>
</head>
<body>

<section class="card card-front" aria-label="Card front">
  <div class="brand">
    <span class="brand-dot"></span>
    <p class="brand-name">Brindlecrest<span class="brand-tag">Risk &amp; Planning</span></p>
  </div>
</section>

<section class="card card-back" aria-label="Card back">
  <div class="brand">
    <span class="brand-dot"></span>
    <p class="brand-name">Brindlecrest<span class="brand-tag">Risk &amp; Planning</span></p>
  </div>

  <div class="person">
    <p class="person-name">Dwight Hollander</p>
    <p class="person-role">Founder &amp; Financial Professional</p>
  </div>

  <div class="divider"></div>

  <ul class="contacts">
    <li>
      <svg viewBox="0 0 16 16" aria-hidden="true"><path d="M3.6 1.2l2.2 2.6-1.2 1.6c.8 1.9 2.2 3.3 4 4.1l1.6-1.2 2.6 2.2-1.3 2.3C6.8 12.7 3.3 9.2 1.4 2.5z"/></svg>
      <span>0455 318 207</span>
    </li>
    <li>
      <svg viewBox="0 0 16 16" aria-hidden="true"><path d="M1 3h14v10H1z M2.5 4.3v.4L8 9l5.5-4.3v-.4z" fill-rule="evenodd"/></svg>
      <span>info@brindlecrestrp.com</span>
    </li>
    <li>
      <svg viewBox="0 0 16 16" aria-hidden="true"><circle cx="8" cy="8" r="7"/><path d="M1.5 8h13 M8 1.2c-2.5 2.5-2.5 11 0 13.6 M8 1.2c2.5 2.5 2.5 11 0 13.6" stroke="#0f2a1f" stroke-width="1.1" fill="none"/></svg>
      <span>www.brindlecrestrp.com</span>
    </li>
  </ul>

  <p class="address">88 Halden Row, Suite 4<br>30217, Aldermere</p>

  <div class="qr-area" role="img" aria-label="QR code linking to the appointment scheduling page"></div>

  <svg class="edge-band" viewBox="0 0 540 18" aria-hidden="true">
    <polygon points="0,10 318,10 310,18 0,18" fill="var(--gold)"/>
    <polygon points="332,4 540,4 540,18 322,18" fill="var(--gold)"/>
  </svg>
</section>

</body>
</html>
```